Business Card design for Property Developer

We need a business card design for a Melbourne based Property Developer called "Kestrelmoor Holdings Pty Ltd".

We subdivide land and onsell to builders etc.

We already have a company logo, which is attached. Also I have attached the layout requirements from the printer. We would like a 2-sided design with one side displaying our logo by itself and the other with the required info, such as name, address, tel no., email, abn etc. The card will need to be used by 4 members of staff so name and contact details should be interchangable.
Updates

If possible, can you please write "name' "job position" "phone" "email" "address" on the card but leave them so I can add the details at a later time. Thank you. Also I plan on printing with UV spot printing as a background on the card. Keep this is mind when designing.

Thanks again.

Hello designers, please do not include pics of houses, house plansĀ or construction machinery etc as we really do not like the way it looks. Thank you.

Target Market(s)

Real Estate Agents, Land Owners, Local Council Departments, Govt Bodies, other Developers etc.

Industry/Entity Type

Business

Requirements
Must have
• 2-sided design with one side displaying our logo by itself and the other with the required info, such as name, address, tel no., email, abn etc.

```html
<!DOCTYPE html>
<html lang="en">
<head>
<meta charset="utf-8">
<title>Kestrelmoor Holdings – Business Card</title>
<link rel="stylesheet" href="https://fonts.googleapis.com/css2?family=Arimo:wght@400;700&family=Cinzel:wght@400&display=swap">
<style>
  :root{
    --page:#d6d6d6;
    --card-white:#f4f4f4;
    --panel-white:#ececec;
    --brand-red:#c40d12;
    --brand-red-dark:#9c0306;
    --brand-red-bright:#e00a0f;
    --brand-blue:#1a3c9c;
    --ink:#1a1a1a;
    --rule:#555555;
    --label:#333333;
  }
  *{margin:0;padding:0;box-sizing:border-box}
  html,body{width:1200px;height:895px;overflow:hidden}
  body{background:var(--page);font-family:"Arimo",Arial,sans-serif;position:relative}

  .card{position:absolute;top:302px;width:569px;height:342px;border-radius:16px;overflow:hidden}
  .card--front{left:18px;background:var(--card-white)}
  .card--back{left:612px;background:var(--brand-red-dark)}

  .front-panel{position:absolute;left:33px;top:36px;width:505px;height:275px;border-radius:22px;overflow:hidden;
    background:linear-gradient(160deg,#fbfbfb 0%,#f0f0f0 55%,#e4e4e4 100%);border:1px solid #e0e0e0}
  .front-texture{position:absolute;right:0;top:0;width:120px;height:100%;
    background:linear-gradient(90deg,rgba(225,225,225,0) 0%,rgba(218,218,218,.55) 100%)}
  .front-texture--left{left:0;right:auto;width:36px;
    background:linear-gradient(270deg,rgba(225,225,225,0) 0%,rgba(218,218,218,.45) 100%)}

  .brand{position:absolute;display:flex;flex-direction:column;align-items:center;text-align:center}
  .brand--front{left:0;right:0;top:52px}
  .brand__mark{border-radius:50%;background:var(--brand-blue)}
  .brand--front .brand__mark{width:100px;height:100px;margin-bottom:12px}
  .brand__name{font-weight:700;color:var(--brand-red);text-transform:uppercase;line-height:1.05}
  .brand--front .brand__name{font-size:27px;letter-spacing:.5px}

  .back-panel{position:absolute;left:32px;top:36px;width:504px;height:273px;border-radius:20px;
    background:radial-gradient(ellipse at 75% 20%,var(--brand-red-bright) 0%,var(--brand-red) 55%,#b0070b 100%)}
  .info-strip{position:absolute;left:62px;top:99px;width:446px;height:134px;border-radius:22px;
    background:linear-gradient(180deg,#ffffff 0%,var(--panel-white) 100%)}
  .brand--back{left:0;width:190px;top:34px}
  .brand--back .brand__mark{width:44px;height:44px;margin-bottom:6px}
  .brand--back .brand__name{font-size:11.5px}
  .info-strip__divider{position:absolute;left:191px;top:10px;width:1px;height:114px;background:var(--rule)}

  .contact{position:absolute;left:217px;top:20px;color:var(--ink);font-size:12px;line-height:13.5px}
  .contact__name{font-size:17px;font-weight:700;color:var(--brand-red);margin-bottom:3px;line-height:18px;padding-left:18px}
  .contact__row{display:flex;align-items:center;gap:6px}
  .contact__row--phone{font-size:14.5px;line-height:13.5px;letter-spacing:.3px}
  .contact__icon{width:12px;height:11px;flex:none}
  .contact__spacer{width:12px;flex:none}

  .side-label{position:absolute;top:686px;font-family:"Cinzel",Georgia,serif;font-size:14px;letter-spacing:3px;color:var(--label)}
  .side-label--front{left:66px}
  .side-label--back{left:660px}
</style>
</head>
<body>

<section class="card card--front" aria-label="Card front">
  <div class="front-panel">
    <div class="front-texture" role="img" aria-label="Faint dotted UV spot texture"></div>
    <div class="front-texture front-texture--left" role="img" aria-label="Faint dotted UV spot texture"></div>
    <div class="brand brand--front">
      <div class="brand__mark"></div>
      <div class="brand__name">Kestrelmoor<br>Holdings</div>
    </div>
  </div>
</section>

<section class="card card--back" aria-label="Card back">
  <div class="back-panel"></div>
  <div class="info-strip">
    <div class="brand brand--back">
      <div class="brand__mark"></div>
      <div class="brand__name">Kestrelmoor<br>Holdings</div>
    </div>
    <div class="info-strip__divider"></div>
    <div class="contact">
      <div class="contact__name">John Doe</div>
      <div class="contact__row"><span class="contact__spacer"></span>www.loremipsum.com</div>
      <div class="contact__row">
        <svg class="contact__icon" viewBox="0 0 12 11" aria-hidden="true"><rect x="0" y="2" width="12" height="9" fill="var(--brand-red)"/><path d="M0 2 L6 7 L12 2" fill="none" stroke="#fff" stroke-width="1.2"/></svg>
        Johndoe@loremipsum.com
      </div>
      <div class="contact__row contact__row--phone">
        <svg class="contact__icon" viewBox="0 0 12 11" aria-hidden="true"><rect x="3" y="0" width="6" height="3" fill="var(--brand-red)"/><rect x="0" y="4" width="12" height="5" rx="1" fill="var(--brand-red)"/><rect x="3" y="8" width="6" height="3" fill="var(--brand-red)"/></svg>
        123 456 7890
      </div>
      <div class="contact__row contact__row--phone">
        <svg class="contact__icon" viewBox="0 0 12 11" aria-hidden="true"><path d="M0 4 Q6 0 12 4 L12 5 L9 5 L8 3.5 L4 3.5 L3 5 L0 5 Z" fill="var(--brand-red)"/><rect x="1.5" y="6" width="9" height="5" rx="1" fill="var(--brand-red)"/></svg>
        123 456 7890
      </div>
      <div class="contact__row contact__row--phone">
        <svg class="contact__icon" viewBox="0 0 12 11" aria-hidden="true"><rect x="0" y="1" width="12" height="10" rx="1" fill="var(--brand-red)"/><rect x="2" y="3" width="3" height="6" fill="#fff"/><rect x="6.5" y="3" width="4" height="2" fill="#fff"/></svg>
        123 456 7890
      </div>
    </div>
  </div>
</section>

<div class="side-label side-label--front">FRONT</div>
<div class="side-label side-label--back">BACK</div>

</body>
</html>
```